7:40 Steady Compass- A Handbook For Shaping Your Daily Conduct Each Morning

7:40 Steady Compass
A Handbook For Shaping Your Daily Conduct Each Morning

It will be a 6 X 9 guide that is meant for people to keep with them with pages to fill out. See supporting pics for overall pillars that are discussed and form basis of the solution.

I will need a spine and back cover as well.

My blog and content: www.morvenqlisk.com

Target Market(s)

Business professionals, senior emergency services people

Industry/Entity Type

Business Management

Font styles to use
Serif

Colors

Designer to choose colors to be used in the design.

Requirements
Must have
• Clean look, easily recognizable among other books. Front cover and back and spine. My picture on the back somewhere (corner maybe?!)
Nice to have
• Easily recognizeable
• NOTE: Graphic should read Today, Was I the Leader That I Would Want? I uploaded graphic that says ..."I Would've Wanted" which is incorrect.
Should not have
• Busy cover

```html
<!DOCTYPE html>
<html lang="en">
<head>
<meta charset="utf-8">
<title>7:40 Steady Compass – Book Cover</title>
<link href="https://fonts.googleapis.com/css2?family=Cinzel:wght@400;500&family=EB+Garamond:wght@400&display=swap" rel="stylesheet">
<style>
  :root {
    --paper: #ececeb;
    --paper-light: #f4f4f3;
    --ink-navy: #16465d;
    --ink-slate: #7f9cab;
    --ink-body: #2f4450;
    --spine: #15455c;
    --spine-ink: #e9eef1;
    --box-line: #1b1b1b;
    --scene-light: #eeeeed;
    --scene-warm: #e6dcdc;
    --scene-cool: #dfe3e8;
  }
  * { margin: 0; padding: 0; box-sizing: border-box; }
  html, body { width: 1200px; height: 864px; overflow: hidden; background: var(--paper); }
  .wrap {
    position: relative; width: 1200px; height: 864px;
    background: radial-gradient(ellipse at 75% 45%, var(--paper-light), var(--paper) 70%);
    font-family: "EB Garamond", Georgia, serif;
  }

  /* Back cover */
  .back-cover { position: absolute; left: 0; top: 0; width: 576px; height: 864px; }
  .back-photo-area {
    position: absolute; left: 262px; top: 18px; width: 52px; height: 76px;
    border-radius: 8px;
    background: linear-gradient(180deg, var(--scene-light), var(--scene-warm));
  }
  .blurb {
    position: absolute; left: 41px; width: 502px;
    font-size: 15.2px; line-height: 17.6px; color: var(--ink-body);
    text-align: justify; hyphens: auto;
  }
  .blurb-one { top: 114px; }
  .blurb-two { top: 307px; }
  .author-photo {
    position: absolute; left: 45px; top: 476px; width: 177px; height: 177px;
    border-radius: 50%;
    background: radial-gradient(circle at 50% 45%, #a3a3a3, #3a3a3a);
  }
  .author-bio {
    position: absolute; left: 239px; top: 485px; width: 297px;
    font-size: 12.3px; line-height: 14.4px; color: var(--ink-body);
    text-align: justify; hyphens: auto;
  }
  .code-box {
    position: absolute; left: 382px; top: 710px; width: 159px; height: 114px;
    background: #fff; border: 1.5px solid var(--box-line);
  }

  /* Spine */
  .spine {
    position: absolute; left: 576px; top: 0; width: 48px; height: 864px;
    background: var(--spine); color: var(--spine-ink);
    font-family: "Cinzel", "Times New Roman", serif;
  }
  .spine-title, .spine-author {
    position: absolute; left: 0; width: 48px;
    writing-mode: vertical-rl; transform: rotate(180deg);
    display: flex; align-items: center; justify-content: center;
    font-size: 27px; line-height: 48px; white-space: nowrap;
    text-transform: uppercase;
  }
  .spine-title { top: 32px; height: 440px; }
  .spine-author { top: 584px; height: 200px; font-size: 24px; }

  /* Front cover */
  .front-cover {
    position: absolute; left: 624px; top: 0; width: 576px; height: 864px;
    text-align: center; font-family: "Cinzel", "Times New Roman", serif;
  }
  .title-number {
    position: absolute; left: 0; width: 576px; top: 12px;
    font-size: 118px; line-height: 1; color: var(--ink-navy); font-weight: 400;
  }
  .title-words {
    position: absolute; left: 0; width: 576px; top: 122px;
    color: var(--ink-navy); font-weight: 400;
  }
  .title-words span { display: block; line-height: 1; }
  .title-line-one { font-size: 86px; }
  .title-line-two { font-size: 92px; margin-top: 4px; }
  .subtitle {
    position: absolute; left: 0; width: 576px; top: 308px;
    font-size: 25px; line-height: 45px; color: var(--ink-slate);
    text-transform: uppercase;
  }
  .front-photo-area {
    position: absolute; left: 48px; top: 472px; width: 488px; height: 256px;
    border-radius: 12px;
    background: linear-gradient(160deg, var(--scene-cool), var(--scene-light) 50%, var(--scene-warm));
  }
  .author-name {
    position: absolute; left: 0; width: 576px; top: 756px;
    font-size: 60px; line-height: 1; color: var(--ink-navy);
    text-transform: uppercase; letter-spacing: -1px; white-space: nowrap;
  }
</style>
</head>
<body>
<main class="wrap">
  <section class="back-cover">
    <div class="back-photo-area" role="img" aria-label="Photo of a single red game pawn on a pale surface"></div>

    <p class="blurb blurb-one">Lorem ipsum dolor sit amet, consectetur adipiscing elit. Nulla dapibus tellus est. Proin vitae ligula lobortis, placerat felis eget, congue arcu. Integer rutrum vitae nulla ac molestie. Integer bibendum id enim quis mattis. Cras et lectus risus. Donec ornare pellentesque justo, nec aliquam magna volutpat ut. Cras eget hendrerit lectus. Proin in mollis sem, ut auctor tellus. Sed ultrices, felis consectetur efficitur ornare, risus lacus auctor turpis, ut commodo elit justo id nulla. Fusce sollicitudin sapien mauris, ut suscipit lorem vestibulum sollicitudin. Sed porta aliquam ex eget elementum. Nulla aliquam scelerisque est vel pellentesque. Vivamus feugiat diam in volutpat imperdiet. Sed congue quam ante. Donec ut viverra nisl. Aenean rhoncus massa ut dui dictum luctus.</p>

    <p class="blurb blurb-two">Nullam mauris nunc, pharetra sit amet ultrices sit amet, rutrum quis orci. Vestibulum eget finibus ligula. Mauris vestibulum nisl sit amet odio imperdiet, non vulputate lacus tempor. Class aptent taciti sociosqu ad litora torquent per conubia nostra, per inceptos himenaeos. Phasellus pellentesque sit amet ligula euismod eleifend. Proin vitae ex quis nibh pretium gravida sit amet eget nulla. Etiam interdum quis nisi id scelerisque. Pellentesque sagittis interdum ante vestibulum interdum. Curabitur ut mauris quam. Donec cursus velit quis erat ultrices convallis. Etiam dignissim eros vel eleifend hendrerit.</p>

    <div class="author-photo" role="img" aria-label="Black and white portrait photo of the author in a circle"></div>

    <p class="author-bio">Lorem ipsum dolor sit amet, consectetur adipiscing elit. Nulla dapibus tellus est. Proin vitae ligula lobortis, placerat felis eget, congue arcu. Integer rutrum vitae nulla ac molestie. Integer bibendum id enim quis mattis. Cras et lectus risus. Donec ornare pellentesque justo, nec aliquam magna volutpat ut. Cras eget hendrerit lectus. Proin in mollis sem, ut auctor tellus. Sed ultrices, felis consectetur efficitur ornare, risus lacus auctor turpis, ut commodo elit justo id nulla. Fusce sollicitudin sapien mauris, ut suscipit lorem vestibulum sollicitudin. Sed porta aliquam ex eget elementum. Nulla aliquam scelerisque est vel pellentesque. Vivamus feugiat diam in volutpat imperdiet. Sed congue quam ante. Donec ut viverra nisl. Aenean rhoncus massa ut dui dictum</p>

    <div class="code-box"></div>
  </section>

  <section class="spine">
    <div class="spine-title">7:40 Steady Compass</div>
    <div class="spine-author">Morven Q. Lisk</div>
  </section>

  <section class="front-cover">
    <h1 class="title-number">7:40</h1>
    <h2 class="title-words">
      <span class="title-line-one">Steady</span>
      <span class="title-line-two">Compass</span>
    </h2>
    <p class="subtitle">A Handbook<br>For Shaping Your Daily Conduct<br>Each Morning</p>

    <div class="front-photo-area" role="img" aria-label="Softly focused photo of coloured game pawns scattered on a pale surface, a red pawn in front"></div>

    <p class="author-name">Morven Q. Lisk</p>
  </section>
</main>
</body>
</html>
```